Rise To Go Further! - Marketing, Training, Managment for Multifamily Professionals

Flyer for training event. I have to be able to edit location, times, speakers, cost,
We will have 2 to 4 speakers for each event. Each event may have a different topic relating to the main topic (Marketing, Training, Management). The idea is to get as many people to open or pick up the fly and say "I have to attend" this seminar. We are the experts in the industry and want to portray this with the flyer. Each speaker will have a topic and a certain amount of time. Each topic will be different.
Updates

Project Deadline Extended
Reason: I apologize for the new design deadline. I've been traveling extensively for work and unable to view submissions. Currently I am not traveling and able to dedicate time to view all of the wonderful submissions. I'm looking forward to selecting one. Thank you all for your understanding.

Target Market(s)

Multifamily - Apartment Communities, Owners, Apartment Associations, Leasing Agents, Marketing Directors, Managers, Presidents,

Industry/Entity Type

Marketing

Colors

Designer to choose colors to be used in the design.

Requirements
Must have
• Editable flyer. I have to be able to edit; location, times/date, speaker, cost, description.
• Sponsored by Tovali Power attached Logo for TVP
Nice to have
• Spot for photo of each speaker (2-4) speaker

```html
<!DOCTYPE html>
<html lang="en">
<head>
<meta charset="utf-8">
<title>Rise To Go Further! – Training Seminar Flyer</title>
<link rel="stylesheet" href="https://fonts.googleapis.com/css2?family=Lato:wght@400;700&family=Montserrat:wght@500;700&family=Roboto+Condensed:wght@300;400;700&display=swap">
<style>
  :root {
    --backdrop: #e4e4e4;
    --panel-top: #dedede;
    --panel-bottom: #f6f6f6;
    --white: #ffffff;
    --ink: #2b2b2b;
    --ink-soft: #333333;
    --magenta: #e0158f;
    --sky: #2fa7d8;
    --cta: #29abe2;
    --cta-fold: #1a6f8f;
    --sun: #fbd400;
    --grape: #4a4284;
    --leaf: #5c9a58;
    --label-green: #5e8a5e;
    --photo-pale: #ede9dc;
    --photo-mid: #c9c6c0;
    --photo-dark: #8c8c8a;
  }
  * { box-sizing: border-box; margin: 0; padding: 0; }
  html, body { width: 1200px; height: 1200px; overflow: hidden; background: var(--backdrop); }
  .flyer {
    position: absolute; left: 233px; top: 81px;
    width: 918px; height: 1298px;
    transform: scale(0.8); transform-origin: top left;
    background: var(--white);
    font-family: "Lato", sans-serif; color: var(--ink);
  }
  .speakers-panel {
    position: absolute; left: 0; top: 0; width: 482px; height: 1280px;
    background: linear-gradient(180deg, var(--panel-top), var(--panel-bottom));
  }
  .footer-band { position: absolute; left: 0; bottom: 0; width: 100%; height: 18px; background: var(--sun); }

  .tile { position: absolute; }
  .tile--sky { background: var(--sky); }
  .tile--sun { background: var(--sun); }
  .tile--magenta { background: var(--magenta); }
  .tile--grape { background: var(--grape); }
  .tile--leaf { background: var(--leaf); }
  .tile--photo { background: linear-gradient(135deg, var(--photo-pale), var(--photo-mid)); }
  .tile--photo-dark { background: linear-gradient(135deg, var(--photo-mid), var(--photo-dark)); }

  .speaker-card {
    position: absolute; width: 187px; height: 190px; background: var(--white);
    box-shadow: 0 8px 8px -6px rgba(0,0,0,0.35);
  }
  .speaker-photo {
    height: 145px;
    background: radial-gradient(circle at 50% 40%, #5a5a5a 0 30%, #ffffff 31%);
  }
  .speaker-label {
    height: 45px; background: var(--label-green); text-align: center; color: var(--ink);
  }
  .speaker-label small { display: block; font-size: 9px; font-weight: 700; color: var(--white); padding-top: 7px; }
  .speaker-label span { display: block; font-size: 16px; letter-spacing: 0.3px; color: #1f2a1f; margin-top: 2px; }
  .speaker-bio {
    position: absolute; width: 330px; text-align: center;
    font-size: 15px; line-height: 18.5px; color: var(--ink-soft);
  }

  .event-details { position: absolute; left: 482px; width: 436px; text-align: center; }
  .detail-label { font-family: "Montserrat", sans-serif; font-weight: 500; font-size: 17px; color: var(--magenta); }
  .topic-title { font-family: "Montserrat", sans-serif; font-weight: 700; font-size: 28px; letter-spacing: 1.5px; color: var(--ink); }
  .detail-value { font-family: "Roboto Condensed", sans-serif; font-size: 31px; color: var(--ink); }
  .detail-text { font-size: 16px; line-height: 20px; color: var(--ink-soft); }

  .cta-fold { position: absolute; left: 451px; top: 956px; }
  .cta-band {
    position: absolute; left: 451px; top: 987px; width: 467px; height: 161px;
    background: var(--cta); color: var(--white); text-align: center;
    font-family: "Roboto Condensed", sans-serif;
  }
  .cta-price { font-weight: 300; font-size: 60px; line-height: 1; padding-top: 8px; }
  .cta-action { font-weight: 700; font-size: 74px; line-height: 1; margin-top: 2px; }

  .sponsor {
    position: absolute; left: 600px; top: 1188px; display: flex; align-items: center; gap: 10px;
    font-family: "Lato", sans-serif; font-weight: 700; font-size: 56px; color: #111111;
  }
  .sponsor-mark { width: 18px; height: 18px; background: var(--magenta); }
</style>
</head>
<body>
<main class="flyer">
  <section class="speakers-panel"></section>

  <div class="tile tile--photo" style="left:348px;top:0;width:134px;height:140px" role="img" aria-label="Blurred photo of a seminar room"></div>
  <div class="tile tile--sky" style="left:492px;top:0;width:167px;height:140px"></div>
  <div class="tile tile--photo" style="left:663px;top:0;width:123px;height:140px" role="img" aria-label="Blurred photo of an office interior"></div>
  <div class="tile tile--sun" style="left:796px;top:0;width:122px;height:132px"></div>
  <div class="tile tile--photo" style="left:492px;top:144px;width:167px;height:126px" role="img" aria-label="Blurred photo of seminar attendees"></div>
  <div class="tile tile--magenta" style="left:662px;top:144px;width:126px;height:126px"></div>
  <div class="tile tile--photo" style="left:792px;top:144px;width:126px;height:126px" role="img" aria-label="Blurred photo of professionals in discussion"></div>
  <div class="tile tile--grape" style="left:492px;top:277px;width:165px;height:144px"></div>
  <div class="tile tile--photo-dark" style="left:662px;top:277px;width:126px;height:144px" role="img" aria-label="Blurred photo of a presenter"></div>
  <div class="tile tile--leaf" style="left:794px;top:277px;width:124px;height:144px"></div>
  <div class="tile tile--sun" style="left:662px;top:428px;width:126px;height:143px"></div>
  <div class="tile tile--photo-dark" style="left:796px;top:428px;width:122px;height:143px" role="img" aria-label="Blurred photo of a meeting"></div>

  <article class="speaker-card" style="left:131px;top:85px">
    <div class="speaker-photo" role="img" aria-label="Speaker photo placeholder"></div>
    <div class="speaker-label"><small>SPEAKER NAME :</small><span>LOREM IPSUM</span></div>
  </article>
  <p class="speaker-bio" style="left:65px;top:297px">Lorem Ipsum is simply dummy text of the printing and typesetting industry. Lorem Ipsum has been the industry's standard dummy text</p>

  <article class="speaker-card" style="left:131px;top:366px">
    <div class="speaker-photo" role="img" aria-label="Speaker photo placeholder"></div>
    <div class="speaker-label"><small>SPEAKER NAME :</small><span>LOREM IPSUM</span></div>
  </article>
  <p class="speaker-bio" style="left:65px;top:578px">Lorem Ipsum is simply dummy text of the printing and typesetting industry. Lorem Ipsum has been the industry's standard dummy text</p>

  <article class="speaker-card" style="left:137px;top:669px">
    <div class="speaker-photo" role="img" aria-label="Speaker photo placeholder"></div>
    <div class="speaker-label"><small>SPEAKER NAME :</small><span>LOREM IPSUM</span></div>
  </article>
  <p class="speaker-bio" style="left:65px;top:881px">Lorem Ipsum is simply dummy text of the printing and typesetting industry. Lorem Ipsum has been the industry's standard dummy text</p>

  <article class="speaker-card" style="left:131px;top:953px">
    <div class="speaker-photo" role="img" aria-label="Speaker photo placeholder"></div>
    <div class="speaker-label"><small>SPEAKER NAME :</small><span>LOREM IPSUM</span></div>
  </article>
  <p class="speaker-bio" style="left:59px;top:1171px">Lorem Ipsum is simply dummy text of the printing and typesetting industry. Lorem Ipsum has been the industry's standard dummy text</p>

  <div class="event-details" style="top:606px"><p class="detail-label">TOPIC NAME</p></div>
  <div class="event-details" style="top:631px"><h1 class="topic-title">LOREM IPSUM</h1></div>
  <div class="event-details" style="top:695px"><p class="detail-label">DATE:</p></div>
  <div class="event-details" style="top:722px"><p class="detail-value">XX/ XX/2017</p></div>
  <div class="event-details" style="top:792px"><p class="detail-label">TIME:</p></div>
  <div class="event-details" style="top:816px"><p class="detail-value">9am to 4pm</p></div>
  <div class="event-details" style="top:886px"><p class="detail-label">LOCATION:</p></div>
  <div class="event-details" style="top:919px"><p class="detail-text">Lorem Ipsum is simply dummy text of the printing<br>and typesetting industry.</p></div>

  <svg class="cta-fold" width="31" height="31" viewBox="0 0 31 31"><polygon points="0,31 31,0 31,31" fill="var(--cta-fold)"/></svg>
  <div class="cta-band">
    <p class="cta-price">ONLY $XX</p>
    <p class="cta-action">BOOK NOW</p>
  </div>

  <div class="sponsor"><span>TVP</span><span class="sponsor-mark"></span></div>

  <div class="footer-band"></div>
</main>
</body>
</html>
```